Veteran owned/staffed Organization that hires Veterans into Ironworking

Please see attached documents for all details and info.
We want a tri-fold brochure to use as a recruiting tool.
Our slogan is:
"Revolutionizing the skilled workforce, one Veteran at a time"
Veteran Apprenticeship Program in Ironworking
Skills/Traits: Welding, bolting, rigging, connecting
Teamwork, camaraderie, GI Bill, Skilled Labor, Career, Community service
OJT, Apprenticeship, Career
Due to the large number of retirees from the baby boomer generation, ironworkers are in high demand. In Texas, the construction industry is on the rise and due to our training regiment, an average of 40 hrs/wk are worked. Our apprenticeship program follows the PLOWD curriculum and at the end of the 3-year course involving classroom learning, OJT and practical application the apprentice achieves journeymen status in ironworking. Journeyman status opens the door to possible postions like foremen, crane operators and project managers. Ironworkers perform their duties on steel structures that provide a skeleton for commercial buildings like hospitals, schools and skyscrapers. Some of the key skilled trades of ironworking are welding, rigging, bolting and connecting.
All Things Veterans
Camaraderie and Culture
-Veteran owned and majority staffed organization who are committed to the mission of providing opportunitites to Veterans
-Graduation celebration after completion of initial training period, holiday parties and get togethers at OKDs
-Work with other Veterans and always have your teammate’s six
-We’re building America, one Veteran career at a time
Professional Support
BRT is committed to providing Veterans with supportive services designed to assist you and your families in the following areas:
Financial, family and work-related support.
Community Service
Disaster Response
Louisiana Flooding - Sept 2016
As the 15th anniversery of 9/11 approached BRT worked to find a volunteer opportunity. An ambitious plan was formed to respond to the devastating 1000-year flood event in Baton Rouge. With little time for planning, BRT organized all the tools and supplies necessary to take 24 Veterans to assist a community in extreme poverty. The team gutted the homes of nine residents which included: single mothers, handicapped elderaly and a Korean War Veterans
Hurricane Matthew - Oct 2016
In a period of 24 hours BRT mobilized 16 Veterans with the supplies neccessary to be 100% self-reliant. The team arrived in Holly Hill, SC 8 hours after Hurrican Matthew made landfall. During a period of 2 days, BRT provided over 5,000 meals, distributed 40,000 bottles of water and removed nearly 100 trees.

Target Market(s)

Veterans who are interested in becoming Ironworkers. Usually under the age of 40, have served in the military and are in the Texas area.

Industry/Entity Type

Construction

Font styles to use
Other font styles liked:
• Microgramma in some places (Logo font) and Serif type font for the bulk

Requirements
Must have
• The colors and logo mentioned in the template guidelines document.
• The slogan
• "Revolutionizing the skilled workforce, one Veteran at a time"
Nice to have
• Some charts and graphs if possible?

```html
<!DOCTYPE html>
<html lang="en">
<head>
<meta charset="utf-8">
<title>BRT Tri-fold Brochure</title>
<link href="https://fonts.googleapis.com/css2?family=Michroma&family=Tinos:wght@400;700&display=swap" rel="stylesheet">
<style>
  :root{
    --navy:#13203a;
    --navy-deep:#0e1830;
    --steel-blue:#1f4d74;
    --panel-blue:#27557d;
    --slate:#3b3d44;
    --gold:#c9963f;
    --gold-light:#e2b868;
    --paper:#eff0f2;
    --ink:#1b2233;
    --backdrop:#8c8c8c;
    --white:#ffffff;
  }
  *{margin:0;padding:0;box-sizing:border-box}
  html,body{width:923px;height:1200px;overflow:hidden;background:var(--backdrop)}
  .stage{position:absolute;left:0;top:0;width:1000px;height:1300px;transform:scale(.923);transform-origin:0 0}
  .spread{position:absolute;left:108px;width:787px;height:612px;overflow:hidden;box-shadow:0 4px 14px rgba(0,0,0,.45);background:var(--navy)}
  .spread--outside{top:28px}
  .spread--inside{top:660px;background:var(--paper)}
  .spread > svg{position:absolute;left:0;top:0;width:787px;height:612px}
  .txt{position:absolute;color:var(--white);font-family:"Tinos",serif}
  .display{font-family:"Michroma",sans-serif;font-weight:400;letter-spacing:.3px;white-space:nowrap}

  .about-title{left:30px;top:76px;font-size:15px;padding-bottom:4px;border-bottom:1px solid var(--white)}
  .about-copy{left:30px;top:110px;width:207px;font-size:10.4px;line-height:12.8px;text-align:justify}
  .about-copy p + p{margin-top:11px}

  .brand{position:absolute;text-align:center;color:var(--gold);white-space:nowrap}
  .brand__name{font-family:"Michroma",sans-serif;font-weight:400;font-size:22px;letter-spacing:2px;display:flex;align-items:center;justify-content:center;gap:8px}
  .brand__dot{width:9px;height:9px;background:var(--gold);border-radius:50%}
  .brand__full{font-family:"Michroma",sans-serif;font-size:6.5px;letter-spacing:.8px;margin-top:4px}
  .brand--top{left:320px;top:56px;width:160px}
  .brand--back{left:570px;top:500px;width:160px}

  .slogan{right:15px;top:362px;text-align:right;font-family:"Michroma",sans-serif;font-weight:400;line-height:1.45;white-space:nowrap}
  .slogan span{display:block}
  .slogan .s1{font-size:13px}
  .slogan .s2{font-size:10.5px}
  .slogan .s3{font-size:12px}
  .slogan .s4{font-size:18px;margin-top:1px}

  .contact{right:280px;top:486px;text-align:right;white-space:nowrap}
  .contact__title{font-family:"Michroma",sans-serif;font-weight:400;font-size:14px;padding-bottom:3px;border-bottom:1px solid var(--white);display:inline-block}
  .contact__org{font-weight:700;font-size:10px;margin-top:8px}
  .contact__line{font-size:9.5px;margin-top:9px;display:flex;justify-content:flex-end;align-items:center;gap:5px}
  .contact__square{width:9px;height:9px;background:var(--steel-blue);display:inline-block}

  .url{position:absolute;top:581px;width:240px;display:flex;align-items:center;justify-content:center;gap:6px;font-family:"Michroma",sans-serif;font-size:11px;color:var(--white);white-space:nowrap}
  .url::before,.url::after{content:"";width:18px;height:1px;background:var(--white);opacity:.8}

  .tag{position:absolute;top:187px;width:220px;height:28px;display:flex;align-items:center;justify-content:center;font-family:"Michroma",sans-serif;font-weight:400;font-size:11.5px;white-space:nowrap;background:var(--navy);color:var(--white)}
  .tag--light{background:var(--white);color:var(--navy);border:2px solid var(--navy);outline:1px solid var(--white)}
  .subhead{position:absolute;top:226px;width:230px;text-align:center;font-family:"Tinos",serif;font-weight:700;font-size:15.5px;color:var(--navy);white-space:nowrap}
  .subhead--light{color:var(--white)}
  .body{position:absolute;top:266px;width:232px;font-family:"Tinos",serif;font-size:9px;line-height:11px;color:var(--ink);text-align:justify}
  .body p + p{margin-top:10px}
  .checklist{list-style:none}
  .checklist li{display:flex;gap:7px;margin-bottom:12px}
  .checklist svg{flex:0 0 10px;width:10px;height:10px;margin-top:1px}
  .checklist--light{color:var(--white);text-align:left}
  .event__title{font-weight:700;font-size:10px;color:var(--ink);display:flex;gap:7px;align-items:center}
  .event__copy{padding-left:17px;margin-top:4px;margin-bottom:10px;line-height:10.5px}
</style>
</head>
<body>
<div class="stage">

  <section class="spread spread--outside" aria-label="Brochure outside">
    <svg viewBox="0 0 787 612">
      <defs>
        <linearGradient id="gold" x1="0" y1="0" x2="1" y2="0">
          <stop offset="0" stop-color="#a8752c"/><stop offset=".5" stop-color="#e6bc6c"/><stop offset="1" stop-color="#b07e33"/>
        </linearGradient>
        <linearGradient id="sky" x1="0" y1="0" x2="0" y2="1">
          <stop offset="0" stop-color="#7fa9d4"/><stop offset=".55" stop-color="#b9cbdc"/><stop offset="1" stop-color="#6a5446"/>
        </linearGradient>
        <linearGradient id="weld" x1="0" y1="0" x2="1" y2="1">
          <stop offset="0" stop-color="#5c5a52"/><stop offset=".5" stop-color="#8f8a72"/><stop offset="1" stop-color="#3a3936"/>
        </linearGradient>
      </defs>
      <rect width="787" height="612" fill="var(--navy)"/>
      <polygon role="img" aria-label="Photo: ironworkers in safety harnesses standing on a steel roof frame against the sky" points="267,0 787,0 787,272 267,470" fill="url(#sky)"/>
      <polygon points="532,412 787,272 787,446" fill="var(--panel-blue)"/>
      <polygon role="img" aria-label="Photo: ironworker in a hard hat on a steel beam" points="72,0 267,0 267,112" fill="#6d8fb3"/>
      <line x1="72" y1="0" x2="267" y2="112" stroke="url(#gold)" stroke-width="4"/>
      <polygon role="img" aria-label="Photo: welder in a helmet working on steel in a workshop" points="0,340 320,488 240,585 0,585" fill="url(#weld)"/>
      <line x1="0" y1="338" x2="345" y2="497" stroke="url(#gold)" stroke-width="5"/>
      <line x1="267" y1="470" x2="787" y2="272" stroke="var(--navy-deep)" stroke-width="2"/>

      <g transform="translate(137,294)">
        <circle r="67" fill="none" stroke="var(--white)" stroke-width="2"/>
        <path d="M0,0 L0,-62 A62,62 0 0 0 -53.7,31 Z" fill="var(--steel-blue)" stroke="var(--white)" stroke-width="3"/>
        <path d="M0,0 L0,-62 A62,62 0 0 1 53.7,31 Z" fill="var(--panel-blue)" stroke="var(--white)" stroke-width="3"/>
        <path d="M0,0 L53.7,31 A62,62 0 0 1 -53.7,31 Z" fill="var(--slate)" stroke="var(--white)" stroke-width="3"/>
        <g fill="var(--white)">
          <circle cx="-34" cy="-42" r="3"/><rect x="-37" y="-38" width="6" height="10" rx="1"/>
          <circle cx="-24" cy="-40" r="2.5"/><rect x="-26.5" y="-37" width="5" height="8" rx="1"/>
          <rect x="18" y="-44" width="14" height="4" rx="2"/><rect x="18" y="-39" width="14" height="4" rx="2"/><rect x="18" y="-34" width="14" height="4" rx="2"/>
          <circle cx="0" cy="13" r="6"/><rect x="-8" y="18" width="16" height="6" rx="2"/>
        </g>
        <g font-family="Tinos, serif" font-size="10" fill="var(--white)" text-anchor="middle">
          <text x="-28" y="-15">Family</text><text x="-28" y="-4">support</text>
          <text x="28" y="-15">Financial</text><text x="28" y="-4">support</text>
          <text x="0" y="38">Workplace</text><text x="0" y="49">support</text>
        </g>
      </g>
    </svg>

    <h2 class="txt display about-title">ABOUT US</h2>
    <div class="txt about-copy">
      <p>Bedrock Rigging Trades partners with employers to develop skilled ironworkers from qualified U.S. Military Veterans at no cost to the Veteran. Veterans are employed, trained and join companies and crews with other Veterans.</p>
      <p>BRT is committed to providing Veterans with supportive services designed to assist you and your families in the following areas:</p>
    </div>

    <div class="brand brand--top">
      <div class="brand__name"><span class="brand__dot"></span>BRT</div>
      <div class="brand__full">BEDROCK RIGGING TRADES</div>
    </div>

    <h1 class="txt slogan">
      <span class="s1">REVOLUTIONIZING</span>
      <span class="s2">THE SKILLED WORKFORCE,</span>
      <span class="s3">ONE VETERAN</span>
      <span class="s4">AT A TIME</span>
    </h1>

    <div class="txt contact">
      <h2 class="contact__title">Contact Us</h2>
      <div class="contact__org">Bedrock Rigging Trades, Inc.</div>
      <div class="contact__line">Recruiting@BRTTexas.com</div>
      <div class="contact__line"><span class="contact__square"></span>/BRTTexas</div>
    </div>

    <div class="brand brand--back">
      <div class="brand__name"><span class="brand__dot"></span>BRT</div>
      <div class="brand__full">BEDROCK RIGGING TRADES</div>
    </div>

    <div class="url" style="left:13px">www.BRTTexas.com</div>
    <div class="url" style="left:275px">www.BRTTexas.com</div>
    <div class="url" style="left:535px">www.BRTTexas.com</div>
  </section>

  <section class="spread spread--inside" aria-label="Brochure inside">
    <svg viewBox="0 0 787 612">
      <defs>
        <linearGradient id="gold2" x1="0" y1="0" x2="1" y2="0">
          <stop offset="0" stop-color="#a8752c"/><stop offset=".5" stop-color="#e6bc6c"/><stop offset="1" stop-color="#b07e33"/>
        </linearGradient>
        <linearGradient id="paper" x1="0" y1="0" x2="1" y2="0">
          <stop offset="0" stop-color="#e4e6ea"/><stop offset=".5" stop-color="#ffffff"/><stop offset="1" stop-color="#e6e7eb"/>
        </linearGradient>
        <linearGradient id="frame" x1="0" y1="0" x2="0" y2="1">
          <stop offset="0" stop-color="#8fb2d6"/><stop offset="1" stop-color="#3c4e68"/>
        </linearGradient>
      </defs>
      <rect width="267" height="612" fill="url(#paper)"/>
      <rect x="267" width="255" height="612" fill="var(--navy)"/>
      <rect x="522" width="265" height="612" fill="url(#paper)"/>

      <polygon role="img" aria-label="Photo: ironworker bolting a red shackle on steel" points="0,0 267,0 267,145 0,115" fill="#8a5a48"/>
      <polygon role="img" aria-label="Photo: Veteran ironworker in a green hard hat with flag bandana" points="267,0 522,0 522,172 267,145" fill="#8c9196"/>
      <polygon role="img" aria-label="Photo: team of Veterans joining hands in a huddle outdoors" points="522,0 787,0 787,110 522,172" fill="#7f7a70"/>
      <polyline points="0,121 267,151 522,178 787,116" fill="none" stroke="url(#gold2)" stroke-width="12"/>

      <polygon role="img" aria-label="Photo: steel roof frame with ironworkers seen from below" points="0,516 267,456 522,481 787,496 787,612 0,612" fill="url(#frame)"/>
      <polyline points="0,512 267,452 522,477 787,492" fill="none" stroke="url(#gold2)" stroke-width="9"/>
      <rect y="580" width="787" height="22" fill="var(--navy)" opacity=".85"/>
    </svg>

    <h2 class="tag" style="left:27px">OUR PROGRAM</h2>
    <h2 class="tag tag--light" style="left:281px">ALL THINGS VETERANS</h2>
    <h2 class="tag" style="left:534px">COMMUNITY SERVICE</h2>

    <h3 class="subhead" style="left:22px">OJT, Apprenticeship and Career</h3>
    <h3 class="subhead subhead--light" style="left:280px">Camaraderie and Culture</h3>
    <h3 class="subhead" style="left:535px">Disaster Response</h3>

    <div class="body" style="left:22px">
      <p>Due to the large number of retirees from the baby boomer generation, ironworkers are in high demand. In Texas, the construction industry is on the rise and due to our training regiment, an average of 40 hrs/wk are worked.</p>
      <p>Our apprenticeship program follows the PLOWD curriculum and at the end of the 2-3 year course involving classroom learning, OJT and practical application the apprentice achieves journeymen status in ironworking. During the course you may also be eligible to receive BAH from your GI Bill. Journeymen status opens the door to possible postions like foremen, crane operators and project managers.</p>
      <p>Ironworkers perform their duties on steel structures that provide a skeleton for commercial buildings like hospitals, schools and skyscrapers. Some of the key skilled trades of ironworking are welding, rigging, bolting and connecting.</p>
    </div>

    <ul class="body checklist checklist--light" style="left:282px;width:218px">
      <li><svg viewBox="0 0 10 10"><rect x=".5" y=".5" width="9" height="9" fill="none" stroke="#fff"/><path d="M2 5l2 2 4-5" fill="none" stroke="#fff" stroke-width="1.4"/></svg><span>Veteran owned and majority staffed organization who are committed to the mission of providing opportunitites to Veterans</span></li>
      <li><svg viewBox="0 0 10 10"><rect x=".5" y=".5" width="9" height="9" fill="none" stroke="#fff"/><path d="M2 5l2 2 4-5" fill="none" stroke="#fff" stroke-width="1.4"/></svg><span>Graduation celebration after completion of initial training period, holiday parties and get togethers at OKDs</span></li>
      <li><svg viewBox="0 0 10 10"><rect x=".5" y=".5" width="9" height="9" fill="none" stroke="#fff"/><path d="M2 5l2 2 4-5" fill="none" stroke="#fff" stroke-width="1.4"/></svg><span>We have partnered and participate with a variety of Veteran Service Organizations to provide networking events, Veteran support and camaraderie</span></li>
      <li><svg viewBox="0 0 10 10"><rect x=".5" y=".5" width="9" height="9" fill="none" stroke="#fff"/><path d="M2 5l2 2 4-5" fill="none" stroke="#fff" stroke-width="1.4"/></svg><span>Work with other Veterans and always have your teammate's six</span></li>
    </ul>

    <div class="body" style="left:539px;width:226px">
      <div class="event__title"><svg viewBox="0 0 10 10" width="10" height="10"><rect x=".5" y=".5" width="9" height="9" fill="none" stroke="#13203a"/><path d="M2 5l2 2 4-5" fill="none" stroke="#13203a" stroke-width="1.4"/></svg>Louisiana Flooding - Sept 2016</div>
      <p class="event__copy">As the 15th anniversery of 9/11 approached BRT worked to find a volunteer opportunity. An ambitious plan was formed to respond to the devastating 1000-year flood event in Baton Rouge. With little time for planning, BRT organized all the tools and supplies necessary to take 24 Veterans to assist a community in extreme poverty. The team gutted the homes of nine residents which included: single mothers, handicapped elderaly and a Korean War Veterans</p>
      <div class="event__title"><svg viewBox="0 0 10 10" width="10" height="10"><rect x=".5" y=".5" width="9" height="9" fill="none" stroke="#13203a"/><path d="M2 5l2 2 4-5" fill="none" stroke="#13203a" stroke-width="1.4"/></svg>Hurricane Matthew - Oct 2016</div>
      <p class="event__copy">In a period of 24 hours BRT mobilized 16 Veterans with the supplies neccessary to be 100% self-reliant. The team arrived in Holly Hill, SC 8 hours after Hurrican Matthew made landfall. During a period of 2 days, BRT provided over 5,000 meals, distributed 40,000 bottles of water and removed nearly 100 trees.</p>
    </div>

    <div class="url" style="left:13px;top:579px">www.BRTTexas.com</div>
    <div class="url" style="left:275px;top:579px">www.BRTTexas.com</div>
    <div class="url" style="left:535px;top:579px">www.BRTTexas.com</div>
  </section>

</div>
</body>
</html>
```